Hello!

I need a 4.25x6.87 RVQ paperback cover and OZM audiobook square cover with the same design. Title is "7 SIMPLE NOTES ON A HIGHLAND RETREAT: A Packing, Hiking, and Recovery Handbook". Book is 75 pages long.

Originally I typed the prompt of, "A man with aviator goggles and a scarf flying an Amanita Muscaria mushroom," into ChatGPT to create something of the idea I had in mind (image attached).

IMPORTANT: "Amanita Muscaria" mushroom is now inconsistent with the "Psilocybin" in the title, so if you go this route, you might want to look up something like "golden teacher psilocybin mushroom" to get a better idea of the kind of mushroom I need in the image.

Back Sleeve Summary:
Do you have a blossoming interest in mushrooms? Looking for a manual that’s less science-y and more practical? In search of something that skips the history and gets straight to what’s relevant? Well, then, here’s a pocket-sized guide of what you need to know to have a good experience. This succinct foundation of knowledge was written by someone who has tripped countless times with various-sized doses. Topics covered include set and setting, tripping with others, expectations, intentions, dosage, and more. If you’re ready to explore, then let’s dive right in.

Author Section (with attached photo):
Dorian Belcastro earned a B.S. in Kinesiology from the Harrowgate State University, and has furthered his studies in the fields of psychedelics, psychology, and trauma healing since 2012. He’s been exploring the benefits of psychedelics within himself for equally as long.

• 4.25x6.87 paperback cover (70-75 pages) and OZM audiobook square cover

```html
<!DOCTYPE html>
<html lang="en">
<head>
<meta charset="utf-8">
<title>7 Simple Notes on a Highland Retreat — Cover Spread</title>
<link rel="stylesheet" href="https://fonts.googleapis.com/css2?family=Titan+One&family=Arimo:wght@400&family=Tinos:wght@400&display=swap">
<style>
  :root {
    --backdrop: #dcdcdc;
    --cover-black: #000000;
    --ink-white: #ffffff;
    --accent-yellow: #f5ec1c;
    --accent-cyan: #1fb6d6;
    --accent-magenta: #b13ce0;
    --accent-violet: #7a2bd0;
    --photo-grey: #8a8a8a;
  }
  * { margin: 0; padding: 0; box-sizing: border-box; }
  html, body {
    width: 1200px; height: 603px; overflow: hidden;
    background: var(--backdrop);
  }
  .canvas {
    position: relative; width: 1200px; height: 603px;
    display: flex; align-items: center; justify-content: center;
  }
  .cover-spread {
    position: relative; width: 707px; height: 540px;
    background: var(--cover-black); color: var(--ink-white);
  }

  /* Back cover */
  .back-summary {
    position: absolute; left: 39px; top: 88px; width: 258px;
    font-family: "Arimo", Arial, sans-serif;
    font-size: 10.2px; line-height: 13px; text-align: justify;
  }
  .author-photo {
    position: absolute; left: 39px; top: 258px; width: 86px; height: 103px;
    border: 3px solid var(--ink-white);
    background: linear-gradient(160deg, #5c5c5c, #b8b8b8 55%, #3a3a3a);
  }
  .author-name-back {
    position: absolute; left: 132px; top: 329px;
    font-family: "Titan One", "Arial Black", sans-serif;
    font-size: 14px; line-height: 17px; color: var(--accent-yellow);
    letter-spacing: 0.3px;
  }
  .author-bio {
    position: absolute; left: 39px; top: 367px; width: 258px;
    font-family: "Arimo", Arial, sans-serif;
    font-size: 10.2px; line-height: 13px; text-align: justify;
  }

  /* Front cover */
  .front-cover {
    position: absolute; left: 390px; top: 0; width: 317px; height: 540px;
    text-align: center;
  }
  .title-line-one {
    position: absolute; left: 0; right: 0; top: 14px;
    font-family: "Titan One", "Arial Black", sans-serif;
    font-size: 27px; color: var(--accent-yellow); letter-spacing: 0.5px;
  }
  .title-line-two {
    position: absolute; left: 0; right: 0; top: 52px;
    font-family: "Titan One", "Arial Black", sans-serif;
    font-size: 16px; color: var(--accent-cyan);
  }
  .title-line-three {
    position: absolute; left: 0; right: 0; top: 76px;
    font-family: "Titan One", "Arial Black", sans-serif;
    font-size: 24px; color: var(--accent-magenta); letter-spacing: 0.3px;
    text-shadow: -2px -2px 0 var(--accent-cyan), 2px 2px 0 var(--accent-yellow);
  }
  .cover-art {
    position: absolute; left: 33px; top: 151px; width: 235px; height: 277px;
  }
  .subtitle {
    position: absolute; left: 0; right: 0; top: 443px;
    font-family: "Tinos", "Times New Roman", serif;
    font-size: 13px; line-height: 17px; letter-spacing: 0.4px;
  }
  .author-name-front {
    position: absolute; left: 0; right: 0; top: 492px;
    font-family: "Titan One", "Arial Black", sans-serif;
    font-size: 21px; color: var(--accent-yellow); letter-spacing: 0.5px;
    text-shadow: 2px 2px 0 var(--accent-magenta);
  }
</style>
</head>
<body>
<main class="canvas">
  <section class="cover-spread">
    <p class="back-summary">Do you have a blossoming interest in mushrooms? Looking for a manual that’s less science-y and more practical? In search of something that skips the history and gets straight to what’s relevant? Well, then, here’s a pocket-sized guide of what you need to know to have a good experience. This succinct foundation of knowledge was written by someone who has tripped countless times with various-sized doses. Topics covered include set and setting, tripping with others, expectations, intentions, dosage, and more. If you’re ready to explore, then let’s dive right in.</p>

    <div class="author-photo" role="img" aria-label="Black and white portrait of the author seated in a white shirt"></div>
    <h2 class="author-name-back">DORIAN<br>BELCASTRO</h2>
    <p class="author-bio">earned a B.S. in Kinesiology from Harrowgate State University, and has furthered his studies in the fields of psychedelics, psychology, and trauma healing since 2012. He’s been exploring the benefits of psilocybin and other psychedelics within himself for equally as long.</p>

    <div class="front-cover">
      <h1>
        <span class="title-line-one">7 SIMPLE NOTES</span>
        <span class="title-line-two">ON A</span>
        <span class="title-line-three">HIGHLAND RETREAT</span>
      </h1>

      <svg class="cover-art" viewBox="0 0 235 277" role="img" aria-label="Yellow illustration of a hand holding up a mushroom, with sunburst rays inside a rounded frame">
        <defs>
          <radialGradient id="art-glow" cx="50%" cy="45%" r="60%">
            <stop offset="0%" stop-color="#d9d021"/>
            <stop offset="55%" stop-color="#5a5610"/>
            <stop offset="100%" stop-color="#000000"/>
          </radialGradient>
        </defs>
        <rect x="2" y="2" width="231" height="273" rx="16" fill="url(#art-glow)" stroke="var(--accent-yellow)" stroke-width="2.5"/>
        <circle cx="117" cy="142" r="82" fill="none" stroke="var(--accent-violet)" stroke-width="1.5"/>
      </svg>

      <p class="subtitle">A PACKING, HIKING,<br>AND RECOVERY HANDBOOK</p>
      <p class="author-name-front">DORIAN BELCASTRO</p>
    </div>
  </section>
</main>
</body>
</html>
```